Velko Orthotics Promotional Brochure

We require a brochure to promote Velko Orthotics manufacturing of custom foot orthotics to podiatrists. The design should have an active lifestyle and medical feel / look to it, clean and concise.

Ultimately the main point we want to get across is we make great orthotics in and industry leading turnaround time of 2 days! No other orthotic manufacturer can touch that.

I have attached some images for your use, but don't feel obligated to use them, please be creative and use what you like. THANKS!!

Project Deadline Extended

Deadline has been extended by 5 days. Thank-you.

Promotional

```html
<!DOCTYPE html>
<html lang="en">
<head>
<meta charset="utf-8">
<title>Velko Orthotics Brochure</title>
<link href="https://fonts.googleapis.com/css2?family=Source+Sans+3:wght@400;600;700;900&display=swap" rel="stylesheet">
<style>
  :root{
    --page-bg:#e9ebee;
    --paper:#ffffff;
    --ink:#1d1d1f;
    --brand-blue:#2f7fc1;
    --heading-blue:#1f6fb3;
    --wave-deep:#0e5fa8;
    --wave-mid:#3d9ad8;
    --wave-light:#a9d6f2;
    --label-bar:#dfe6f3;
    --accent-green:#7ab51d;
    --photo-green:#8fb46a;
    --photo-sky:#dfe9d2;
  }
  *{box-sizing:border-box;margin:0;padding:0}
  html,body{width:1200px;height:1000px;overflow:hidden}
  body{background:var(--page-bg);font-family:"Source Sans 3",Arial,sans-serif;color:var(--ink)}
  .brochure{position:absolute;left:50px;top:75px;width:1100px;height:850px;background:var(--paper);overflow:hidden;box-shadow:0 2px 10px rgba(0,0,0,.15)}
  .wave-band{position:absolute;left:0;bottom:0;width:1100px;height:260px}
  .panel{position:absolute;top:0;height:850px;width:366px}
  .panel--left{left:0}
  .panel--middle{left:367px}
  .panel--right{left:734px}
  .heading{color:var(--heading-blue);font-weight:400;font-size:28px;line-height:1}
  .body-copy{font-size:16px;line-height:1.25}
  .body-copy p+p{margin-top:18px}

  .logo{position:absolute;left:36px;top:34px;display:flex;align-items:center;gap:12px}
  .logo__dot{width:46px;height:46px;border-radius:50%;background:var(--brand-blue)}
  .logo__name{font-size:26px;color:var(--ink);font-weight:400}
  .panel--left .heading{position:absolute;left:36px;top:150px}
  .photo{position:absolute}
  .photo--consult{left:36px;top:190px;width:290px;height:150px;background:linear-gradient(120deg,#f1e5dc 0%,#d9c2b2 45%,#5d8fc9 100%)}
  .panel--left .body-copy{position:absolute;left:36px;top:362px;width:310px}
  .photo--therapy{left:150px;top:620px;width:170px;height:230px;background:linear-gradient(180deg,rgba(120,150,190,.55),rgba(40,90,150,.35));border-radius:4px}
  .tagline{position:absolute;left:46px;top:680px;font-size:36px;line-height:1.08;color:var(--ink)}

  .middle-column{position:absolute;left:20px;top:40px;width:330px;display:flex;flex-direction:column}
  .middle-column .heading{margin-bottom:12px}
  .middle-column .body-copy{font-size:15px;line-height:1.22}
  .middle-column .body-copy p+p{margin-top:14px}
  .highlight{color:var(--accent-green);font-weight:700}
  .faster{margin-top:12px;font-size:22px;font-weight:700;color:var(--accent-green);line-height:1.1}
  .materials{margin-top:18px;width:230px;font-size:15px;line-height:1.18}
  .materials__intro{font-weight:700;margin-bottom:6px}
  .materials__group{background:var(--label-bar);font-weight:700;padding:1px 8px;margin:4px 0 2px}
  .materials ul{list-style:none;padding-left:14px}

  .panel--right .heading{position:absolute;left:10px;top:34px}
  .panel--right .body-copy{position:absolute;left:10px;top:80px;width:320px}
  .photo--walk{left:0;top:330px;width:366px;height:520px;background:linear-gradient(180deg,rgba(255,255,255,0) 0%,var(--photo-sky) 18%,var(--photo-green) 60%,#c9c1a8 100%)}
  .badge{position:absolute;left:292px;top:408px;width:56px;height:56px;border-radius:50%;background:var(--brand-blue)}
  .phone{position:absolute;right:14px;top:770px;font-size:40px;font-weight:900;letter-spacing:.5px;color:#111}
</style>
</head>
<body>
<main class="brochure">
  <svg class="wave-band" viewBox="0 0 1100 260" preserveAspectRatio="none" aria-hidden="true">
    <defs>
      <linearGradient id="waveFade" x1="0" x2="1" y1="0" y2="0">
        <stop offset="0" stop-color="#ffffff" stop-opacity="1"/>
        <stop offset="0.65" stop-color="#ffffff" stop-opacity="1"/>
        <stop offset="0.8" stop-color="#ffffff" stop-opacity="0"/>
      </linearGradient>
      <mask id="waveMask"><rect width="1100" height="260" fill="url(#waveFade)"/></mask>
    </defs>
    <g mask="url(#waveMask)">
      <path d="M0 60 C200 0 420 90 700 40 S1000 40 1100 60 V260 H0Z" fill="var(--wave-light)"/>
      <path d="M0 110 C220 40 460 140 720 80 S1000 90 1100 100 V260 H0Z" fill="var(--wave-mid)" opacity=".8"/>
      <path d="M0 170 C240 110 480 200 740 140 S1000 150 1100 160 V260 H0Z" fill="var(--wave-deep)" opacity=".85"/>
      <path d="M0 140 C260 90 500 170 760 120" stroke="#ffffff" stroke-width="3" fill="none" opacity=".8"/>
    </g>
  </svg>

  <section class="panel panel--left">
    <div class="logo"><span class="logo__dot"></span><span class="logo__name">velko orthotics</span></div>
    <h2 class="heading">About Dorian</h2>
    <div class="photo photo--consult" role="img" aria-label="Photo of a clinician examining a patient's shoulder"></div>
    <div class="body-copy">
      <p>Shortly after graduating from physiotherapy in 1995, Dorian began his path to learn more about orthotics and provide excellent orthotic service to his patients.</p>
      <p>He branched out from there, to manufacturing his own orthotics for his patients and then for others. Dorian has been in the orthotic industry for 19 years and his well versed in both clinical and manufacturing of orthotics.</p>
    </div>
    <div class="photo photo--therapy" role="img" aria-label="Photo of a therapist assessing a patient's leg"></div>
    <p class="tagline">fit.<br>function.<br>finish ….<br>faster.</p>
  </section>

  <section class="panel panel--middle">
    <div class="middle-column">
      <h2 class="heading">About Velko</h2>
      <div class="body-copy">
        <p>Velko Orthotics was established in 2007 by Dorian Kessler. Velko mission is to provide the highest quality of orthotics, at fair market price in 2 days turnaround or less. We utilize PFMLA approved practices in custom manufacturing each pair of orthotics.</p>
        <p>We do not use library systems or best fit pre fabs. Velko believes in using technology to help us manufacture great orthotics and not to use technology to be 'THE' manufacturer.! Velko has developed it's own manufacturing process (still utilizing traditional vacuum forming of raw materials to an individually custom designed positive) that improves FF transition, is more accurate and completely reproducible <span class="highlight">for refill orders. …</span></p>
      </div>
      <p class="faster">It's also faster ….<br>way faster!!</p>
      <div class="materials">
        <p class="materials__intro">Velko utilizes the following materials in manufacturing:</p>
        <p class="materials__group">Shellshocked</p>
        <ul><li>Polypropylene</li><li>XR Stride</li><li>EVA</li><li>KTX4</li><li>RL3300!</li></ul>
        <p class="materials__group">Topcovers</p>
        <ul><li>Puff&nbsp; Nevolan&nbsp; Vinyl</li><li>Supraleather</li><li>Softsuede Q-cell!</li></ul>
        <p class="materials__group">Paddings</p>
        <ul><li>Corafoam</li><li>EVA</li></ul>
      </div>
    </div>
  </section>

  <section class="panel panel--right">
    <div class="photo photo--walk" role="img" aria-label="Photo of a family walking together on a sunny park trail"></div>
    <h2 class="heading">Warranty / Guarantee</h2>
    <div class="body-copy">
      <p>Under normal wearing conditions polypropylene and carboplastic shells are guaranteed against breakage for the functional life of the orthotic. !</p>
      <p>Under normal wearing conditions EVA orthotics are guaranteed against excessive compression for 6months.!</p>
      <p>Additions, posts and top covers are guaranteed for 6 months against manufacturing and material defects.</p>
    </div>
    <span class="badge" aria-hidden="true"></span>
    <p class="phone">1.555.210.4477</p>
  </section>
</main>
</body>
</html>
```